New nutrition counseling business needs a flyer and logo design for marketing purposes

Need a new flyer for distribution to advertise and inform the public about new Dietetic Counseling service. The new business name is Harbor of Vigor with “Harbor” being the main name. It will provide nutrition consultation services to individuals who seek to change their dietary habits to achieve a variety of different health objectives. These objectives can include, but are not limited to weight management, enhanced athletic performance, improved health biomarkers, and reducing the risks or symptoms of chronic nutrition related diseases. The services provided include direct one on one counseling that entails health and nutrition assessments, evaluation of goals, and the determination of strategies to meet these goals. We would like to see designs that use an ocean color scheme with purple aspects as well. Color and logo ideas attached in uploads. Please include logo on the flyer as well.

Target Market(s)

General Population

Colors
0094D4
00A9DD
6FCCEA
C7EBF8
E9F6FB
00AB8E
00BBA5
67D7C9
C6EFE9
E9F9F6
6B429C
8869AF
B7A5CE
E3DAEB
F3F0F8

Requirements
Nice to have
• Pictures of nourishing foods, fruits, vegetables etc.
Should not have
• Do not include people in flyer or logo design

```html
<!DOCTYPE html>
<html lang="en">
<head>
<meta charset="utf-8">
<title>Nutrition Consultation Service — Harbor of Vigor</title>
<link rel="stylesheet" href="https://fonts.googleapis.com/css2?family=Bebas+Neue&family=Montserrat:wght@500;600;700;800&display=swap">
<style>
:root{
  --teal:#00BBA5;
  --teal-bright:#14C3A2;
  --blue:#0094D4;
  --green:#8CC657;
  --ink:#141414;
  --white:#ffffff;
  --page:#EEF3F3;
  --mist:#E6E8E8;
}
*{margin:0;padding:0;box-sizing:border-box}
html,body{width:1200px;height:2538px;overflow:hidden;background:var(--page)}
body{position:relative;font-family:"Montserrat",sans-serif;color:var(--ink)}
.flyer{
  position:absolute;left:46px;top:485px;width:1008px;height:1425px;
  transform:scale(1.1);transform-origin:top left;
  background:var(--white);overflow:hidden;
  box-shadow:0 6px 22px rgba(0,0,0,.18);
}
.backdrop{position:absolute;left:0;top:480px;width:1008px;height:945px;
  background:linear-gradient(180deg,#dcdede 0%,#eceeee 45%,#f4f5f5 80%,#fafafa 100%)}
.headline{position:absolute;left:0;top:88px;width:1008px;text-align:center;font-weight:800;line-height:1}
.headline .l1{display:block;color:var(--teal-bright);font-size:86px;letter-spacing:1px}
.headline .l2{display:block;font-size:68px;margin-top:6px;letter-spacing:.5px}
.headline .l3{display:inline-block;color:var(--blue);font-size:58px;margin-top:8px;margin-left:10px;
  padding-bottom:4px;border-bottom:4px solid var(--ink)}
.leaf-mark{position:absolute;border-radius:50%;background:radial-gradient(circle,#a9d46f 0%,#cfe7b3 60%,rgba(255,255,255,0) 72%)}
.leaf-mark.title{left:275px;top:232px;width:100px;height:100px}
.leaf-mark.chat{left:76px;top:1062px;width:120px;height:120px}
.photo-grapes{position:absolute;left:0;top:268px;width:340px;height:190px;border-radius:48% 52% 20% 30%;
  background:radial-gradient(circle at 30% 45%,#b52230 0%,#c9344a 30%,rgba(0,0,0,0) 55%),radial-gradient(circle at 70% 60%,#b9d94a 0%,#cfe67a 35%,rgba(0,0,0,0) 60%),#e9efe1}
.photo-fruit{position:absolute;left:636px;top:118px;width:372px;height:460px;border-radius:40% 10% 30% 45%;
  background:radial-gradient(circle at 55% 30%,#d7a637 0%,#9a8b2c 25%,rgba(0,0,0,0) 45%),radial-gradient(circle at 40% 70%,#f2cf3a 0%,#e9a63a 25%,rgba(0,0,0,0) 45%),radial-gradient(circle at 70% 80%,#b8322f 0%,#7a8f3a 35%,rgba(0,0,0,0) 60%),#eee4cf}
.goal-tag{position:absolute;left:62px;top:387px;width:120px;height:66px;background:var(--blue);color:var(--white);
  font-family:"Bebas Neue",sans-serif;font-size:54px;line-height:70px;text-align:center}
.goal-band{position:absolute;left:62px;top:453px;width:640px;height:82px;background:var(--teal);color:var(--white);
  font-size:24px;font-weight:500;line-height:29px;padding:11px 0 0 16px}
.services-tag{position:absolute;left:58px;top:555px;width:162px;height:46px;background:var(--green);border-radius:8px;
  color:var(--white);font-weight:700;font-size:28px;line-height:44px;text-align:center;box-shadow:0 3px 0 #6f9e3f}
.services{position:absolute;left:58px;top:613px;width:440px;list-style:none;font-size:19.5px;font-weight:500;line-height:22px}
.services li{position:relative;padding-left:23px;margin-bottom:22px}
.services li::before{content:"";position:absolute;left:2px;top:6px;width:8px;height:8px;border-radius:50%;background:var(--teal);box-shadow:0 0 0 3px rgba(0,187,165,.25)}
.modes{position:absolute;left:80px;top:988px;font-size:28px;font-weight:500;line-height:33px}
.modes b,.chat b{color:var(--blue);font-weight:600}
.owner{position:absolute;left:537px;top:630px;width:428px;height:418px;background:var(--teal);border-radius:14px;padding:24px 26px}
.owner .label{display:inline-block;color:var(--white);font-size:31px;font-weight:600;border-bottom:3px solid var(--white);line-height:34px}
.owner .name{font-size:43px;font-weight:600;margin:12px 0 4px;line-height:52px}
.owner ul{list-style:none;margin-top:12px;font-size:20.5px;font-weight:500;line-height:24px}
.owner li{position:relative;padding-left:26px}
.owner li::before{content:"";position:absolute;left:4px;top:7px;width:11px;height:11px;border-radius:50%;background:var(--ink)}
.license{position:absolute;left:43px;top:332px;width:342px;height:60px;border-radius:8px;overflow:hidden;display:flex;
  font-family:"Bebas Neue",sans-serif;font-size:30px;line-height:62px}
.license span:first-child{width:170px;background:var(--white);text-align:center}
.license span:last-child{flex:1;background:var(--green);padding-left:28px}
.chat{position:absolute;left:174px;top:1112px;font-size:26px;font-weight:600;line-height:34px}
.chat .second{display:block;padding-left:110px;color:var(--ink)}
.call{position:absolute;left:40px;top:1272px;font-size:37px;font-weight:600;display:flex;align-items:center;gap:14px}
.call .lead{color:var(--blue)}
.call svg,.mail svg{flex:none}
.mail{position:absolute;left:42px;top:1333px;font-size:33px;font-weight:500;display:flex;align-items:center;gap:20px}
.brand{position:absolute;left:702px;top:1262px;display:flex;align-items:center;gap:12px;color:var(--teal);font-weight:700;font-size:31px}
.brand .dot{width:30px;height:30px;border-radius:50%;background:var(--teal)}
</style>
</head>
<body>
<main class="flyer">
  <div class="backdrop" role="img" aria-label="Faded photo of fresh vegetables"></div>

  <div class="photo-grapes" role="img" aria-label="Photo of red and green grapes"></div>
  <div class="photo-fruit" role="img" aria-label="Photo of pineapple, bananas, papaya, figs, kiwi and berries"></div>

  <h1 class="headline">
    <span class="l1">NUTRITION</span>
    <span class="l2">CONSULTATION</span>
    <span class="l3">SERVICE</span>
  </h1>
  <div class="leaf-mark title" role="img" aria-label="Green leaf ornament"></div>

  <div class="goal-tag">GOAL</div>
  <p class="goal-band">Helping clients foster positive nutrition<br>practices for a healthier lifestyle</p>

  <div class="services-tag">Services</div>
  <ul class="services">
    <li>Medical Nutrition Therapy for chronic conditions such as diabetes, hypertension, high cholesterol, and more</li>
    <li>Weight Management<br>Healthy Eating and Meal Planning</li>
    <li>Nutrition for Athletic Performance</li>
    <li>Pre and Post Natal Nutrition</li>
    <li>Personalized meal plans uniquely catered to each individual</li>
    <li>Highly collaborative approach to help you meet your goals</li>
  </ul>
  <p class="modes">Both in <b>person and virtual<br>consultations</b> are offered</p>

  <section class="owner">
    <span class="label">Owner</span>
    <p class="name">Marisol Delgado</p>
    <span class="label">Credentials</span>
    <ul>
      <li>Master of Science in Dietetics and Nutrition</li>
      <li>Registered Dietitian (RD)</li>
      <li>Licensed Dietitian Nutritionist (LDN)</li>
    </ul>
    <div class="license"><span>LICENSE NUMBER:</span><span>ND 40521.</span></div>
  </section>

  <div class="leaf-mark chat" role="img" aria-label="Green leaf ornament"></div>
  <p class="chat">Let’s Chat! <b>Free 15-minute introductory consultation</b><span class="second">to discuss program details and rates</span></p>

  <p class="call"><span class="lead">Call Today :</span>
    <svg width="30" height="30" viewBox="0 0 24 24" aria-hidden="true"><path fill="#141414" d="M6.6 10.8a15.5 15.5 0 0 0 6.6 6.6l2.2-2.2c.3-.3.7-.4 1-.2 1.1.4 2.3.6 3.6.6.6 0 1 .4 1 1V20c0 .6-.4 1-1 1A17 17 0 0 1 3 4c0-.6.4-1 1-1h3.5c.6 0 1 .4 1 1 0 1.3.2 2.5.6 3.6.1.3 0 .7-.2 1z"/></svg>
    <span>555-014-2287</span></p>
  <p class="mail">
    <svg width="48" height="34" viewBox="0 0 48 34" aria-hidden="true"><rect x="2" y="2" width="44" height="30" fill="none" stroke="#141414" stroke-width="4"/><path d="M2 2l22 17L46 2M2 32l16-15M46 32L30 17" fill="none" stroke="#141414" stroke-width="4"/></svg>
    <span>Marisol@delgadord.net</span></p>

  <div class="brand"><span class="dot"></span><span>Harbor of Vigor</span></div>
</main>
</body>
</html>
```